High-end construction company needs a business card design

We need a modern looking business card that draws people in, is memorable and looks so good people will want to sick it on their fridges.
On the first side what is needed are:
Logo
My name - Tomas Verbelk
Title - Managing Director
Website - www.kravel.co.uk
Email - tomas@kravel.co.uk
Telephone - 020 5194 6381
Mobile - 07845319027
On the back side was is needed is a list of all the services we provide:
-Kitchen Renovations
-Bathroom Renovations
-House Renovations
-Garage Conversions
-Extensions
-Loft Conversions
-Conservatories
-Carpentry
-Tiling
-Electrical
-Plumbing & Heating
-Bricklaying
-Landscaping
-Decorating
-Plastering
We would like the colours to be the same shades as on the logo with grey or black for the words.
Target Market(s)
Anyone who needs building work done
Contact Information for Business Card
This business card is for a construction company which strives to deliver excellent service and quality.
The look and feel of the card should represent this.
Requirements
Must have
- On the first side what is needed are:
Logo
My name - Tomas Verbelk
Title - Managing Director
Website - www.kravel.co.uk
Email - tomas@kravel.co.uk
Telephone - 020 5194 6381
Mobile - 07845319027
Nice to have
- Cool looking features

```html
<!DOCTYPE html>
<html lang="en">
<head>
<meta charset="utf-8">
<title>Kravel Construction Ltd – Business Card</title>
<link rel="stylesheet" href="https://fonts.googleapis.com/css2?family=Lato:wght@400;700&display=swap">
<style>
  :root {
    --page-bg: #f4f4f4;
    --card-white: #ffffff;
    --brand-green: #4b8f3e;
    --accent-green: #6abf45;
    --text-grey: #555555;
    --text-dark: #3a3a3a;
    --shadow: rgba(0, 0, 0, 0.22);
  }
  * { box-sizing: border-box; margin: 0; padding: 0; }
  html, body {
    width: 1200px; height: 1000px; overflow: hidden;
    background: var(--page-bg);
    font-family: "Lato", sans-serif;
  }
  .stage {
    position: absolute; left: 50%; top: 50%;
    width: 1034px; height: 278px;
    transform: translate(-50%, -50%) scale(1.1);
    display: flex; justify-content: space-between;
  }
  .card {
    position: relative; width: 487px; height: 278px;
    box-shadow: 0 6px 10px var(--shadow);
  }
  .brand__mark { width: 9px; height: 9px; background: var(--accent-green); flex: none; }

  /* ---------- Front ---------- */
  .card--front { background: var(--card-white); }
  .front-frame {
    position: absolute; left: 10px; right: 10px; top: 120px; bottom: 9px;
    border: 2px solid var(--accent-green); border-top: none;
  }
  .front-frame__top {
    position: absolute; left: 10px; right: 10px; top: 106px; height: 28px;
    display: flex; align-items: center; gap: 12px;
  }
  .front-frame__top::before,
  .front-frame__top::after {
    content: ""; flex: 1; height: 2px; background: var(--accent-green);
  }
  .brand {
    display: flex; align-items: center; gap: 8px;
    color: var(--accent-green); font-weight: 700; font-size: 18px;
    letter-spacing: 0.06em; text-transform: uppercase; white-space: nowrap;
  }
  .person {
    position: absolute; top: 166px; left: 0; right: 0;
    display: flex; justify-content: center; align-items: center; gap: 12px;
  }
  .person__name { font-size: 20px; font-weight: 700; color: var(--text-grey); }
  .person__title {
    background: var(--accent-green); color: #fff;
    font-size: 13px; padding: 3px 13px 4px;
  }
  .contacts {
    position: absolute; top: 214px; left: 102px; list-style: none;
    display: flex; flex-direction: column; gap: 8px;
  }
  .contact { display: flex; align-items: center; gap: 12px;
    font-size: 12.5px; font-weight: 700; color: var(--text-dark); }
  .contact svg { width: 12px; height: 12px; }
  .phones {
    position: absolute; top: 211px; left: 262px;
    display: flex; align-items: center; gap: 11px;
  }
  .phones__icon { width: 36px; height: 36px; }
  .phones__list { font-size: 11.5px; color: var(--text-dark); line-height: 1.55; }

  /* ---------- Back ---------- */
  .card--back { background: var(--brand-green); }
  .back-frame {
    position: absolute; inset: 10px;
    border: 2px solid var(--card-white);
  }
  .back-tab {
    position: absolute; top: 0; left: 168px; width: 150px; height: 82px;
    background: var(--card-white); border-radius: 0 0 12px 12px;
    display: flex; justify-content: center; align-items: center;
  }
  .back-tab .brand { font-size: 8px; letter-spacing: 0.02em; gap: 4px; }
  .back-tab .brand__mark { width: 6px; height: 6px; }
  .services {
    position: absolute; top: 108px; left: 0; right: 0;
    list-style: none; text-align: center;
    color: #fff; font-size: 13.5px; font-weight: 700;
  }
  .services li { height: 28.5px; }
  .services span + span::before { content: "|"; margin: 0 7px; font-weight: 400; }
</style>
</head>
<body>
<div class="stage">

  <section class="card card--front" aria-label="Business card front">
    <div class="front-frame" aria-hidden="true"></div>
    <div class="front-frame__top">
      <div class="brand"><span class="brand__mark"></span>Kravel Construction Ltd</div>
    </div>

    <div class="person">
      <h1 class="person__name">Tomas Verbelk</h1>
      <span class="person__title">Managing Director</span>
    </div>

    <ul class="contacts">
      <li class="contact">
        <svg viewBox="0 0 12 12" aria-hidden="true"><rect x="0.5" y="0.5" width="11" height="8" rx="1" fill="#6abf45"/><rect x="4" y="9" width="4" height="1.5" fill="#6abf45"/><rect x="2.5" y="10.5" width="7" height="1.2" fill="#6abf45"/></svg>
        www.kravel.co.uk
      </li>
      <li class="contact">
        <svg viewBox="0 0 12 12" aria-hidden="true"><rect x="0.5" y="2" width="11" height="8" fill="#6abf45"/><polyline points="0.8,2.4 6,6.8 11.2,2.4" fill="none" stroke="#fff" stroke-width="1"/></svg>
        tomas@kravel.co.uk
      </li>
    </ul>

    <div class="phones">
      <svg class="phones__icon" viewBox="0 0 36 36" aria-hidden="true">
        <circle cx="18" cy="18" r="18" fill="#6abf45"/>
        <path d="M12.5 10.5c1-1 2.2-.8 2.8.2l1.6 2.7c.5.9.2 1.8-.6 2.4l-.9.7c.7 2 2.2 3.6 4.2 4.5l.8-.9c.7-.8 1.600-1 2.4-.5l2.6 1.7c1 .6 1.1 1.8.2 2.7l-1.2 1.2c-1.5 1.5-4.6.7-7.9-2.5s-4.4-6.6-2.9-8.4z" fill="#fff"/>
      </svg>
      <div class="phones__list">
        <p>020 5194 6381</p>
        <p>07845319027</p>
      </div>
    </div>
  </section>

  <section class="card card--back" aria-label="Business card back">
    <div class="back-frame"></div>
    <div class="back-tab">
      <div class="brand"><span class="brand__mark"></span>Kravel Construction Ltd</div>
    </div>
    <ul class="services">
      <li><span>Kitchen Renovations</span><span>Loft Conversions</span><span>Bricklaying</span></li>
      <li><span>Bathroom Renovations</span><span>Conservatories</span><span>Landscaping</span></li>
      <li><span>House Renovations</span><span>Carpentry</span><span>Decorating</span></li>
      <li><span>Extensions</span><span>Electrical</span><span>Plumbing &amp; Heating</span></li>
      <li><span>Garage Conversions</span><span>Tiling</span><span>Plastering</span></li>
    </ul>
  </section>

</div>
</body>
</html>
```